KRT business cards

I need a Business card design for my self. I am behavior analyst owner of a new company based in Miami. We offer Applied Behavior Analysis (ABA) services to individuals with developmental disabilities.

Business

```html
<!DOCTYPE html>
<html lang="en">
<head>
<meta charset="utf-8">
<title>KRT Business Cards</title>
<link rel="stylesheet" href="https://fonts.googleapis.com/css2?family=Marcellus&family=Open+Sans:wght@400;600&display=swap">
<style>
  :root {
    --backdrop: #ecebe7;
    --card: #ffffff;
    --navy: #1c4a80;
    --green: #4fa447;
    --leaf-soft: #b9ddb4;
    --trunk: #8fabc9;
    --shadow: rgba(0, 0, 0, 0.22);
  }
  * { box-sizing: border-box; margin: 0; padding: 0; }
  html, body {
    width: 1200px;
    height: 900px;
    overflow: hidden;
    background: var(--backdrop);
    font-family: "Open Sans", sans-serif;
  }
  .stage { position: relative; width: 1200px; height: 900px; }
  .card {
    position: absolute;
    width: 560px;
    height: 320px;
    background: var(--card);
    box-shadow: 0 6px 16px var(--shadow);
    overflow: hidden;
  }
  .card--front { left: 50px; top: 140px; }
  .card--back { left: 590px; top: 440px; }

  .decor-tree {
    position: absolute;
    top: 0;
    right: 0;
    width: 260px;
    height: 100%;
  }
  .card--back .decor-tree { right: 150px; width: 230px; }

  .brand {
    position: absolute;
    display: flex;
    flex-direction: column;
    align-items: center;
  }
  .card--front .brand { left: 170px; top: 105px; }
  .card--back .brand { left: 30px; top: 110px; }
  .brand-mark { display: flex; align-items: center; gap: 14px; }
  .brand-dot {
    width: 34px; height: 34px;
    border-radius: 50%;
    background: var(--green);
  }
  .brand-name {
    font-family: "Open Sans", sans-serif;
    font-weight: 600;
    font-size: 58px;
    letter-spacing: 4px;
    color: var(--navy);
    line-height: 1;
  }
  .services {
    margin-top: 22px;
    font-size: 13px;
    line-height: 1.45;
    color: var(--navy);
    text-align: center;
  }
  .services .sep { color: var(--green); padding: 0 3px; }

  .contact-card {
    position: absolute;
    right: 26px;
    top: 118px;
    text-align: right;
  }
  .person-name {
    font-family: "Marcellus", serif;
    font-size: 25px;
    color: var(--navy);
  }
  .person-title {
    font-size: 13px;
    color: var(--green);
    line-height: 1.35;
  }
  .contact-lines {
    position: absolute;
    right: 26px;
    bottom: 34px;
    text-align: right;
    font-size: 15px;
    line-height: 1.6;
  }
  .contact-label { color: var(--navy); font-weight: 600; }
  .contact-value { color: var(--green); }
</style>
</head>
<body>
<main class="stage">

  <section class="card card--front">
    <svg class="decor-tree" viewBox="0 0 260 320" role="img" aria-label="Faint decorative tree with soft green leaves and a curving blue trunk">
      <defs>
        <linearGradient id="tree-front" x1="0" y1="0" x2="1" y2="1">
          <stop offset="0" stop-color="#b9ddb4" stop-opacity="0.85"/>
          <stop offset="1" stop-color="#8fabc9" stop-opacity="0.55"/>
        </linearGradient>
      </defs>
      <rect x="0" y="0" width="260" height="320" fill="url(#tree-front)" opacity="0.45"/>
    </svg>
    <div class="brand">
      <div class="brand-mark">
        <span class="brand-dot"></span>
        <span class="brand-name">KRT</span>
      </div>
      <p class="services">
        Applied Behavior Analysis<span class="sep">|</span>Social Skills Training<br>
        Parent/Teacher Training<span class="sep">|</span>Tutoring
      </p>
    </div>
  </section>

  <section class="card card--back">
    <svg class="decor-tree" viewBox="0 0 230 320" role="img" aria-label="Faint decorative tree with soft green leaves and a curving blue trunk">
      <defs>
        <linearGradient id="tree-back" x1="0" y1="0" x2="1" y2="1">
          <stop offset="0" stop-color="#b9ddb4" stop-opacity="0.85"/>
          <stop offset="1" stop-color="#8fabc9" stop-opacity="0.55"/>
        </linearGradient>
      </defs>
      <rect x="0" y="0" width="230" height="320" fill="url(#tree-back)" opacity="0.45"/>
    </svg>
    <div class="brand">
      <div class="brand-mark">
        <span class="brand-dot"></span>
        <span class="brand-name">KRT</span>
      </div>
      <p class="services">
        Applied Behavior Analysis<span class="sep">|</span>Social Skills Training<br>
        Parent/Teacher Training<span class="sep">|</span>Tutoring
      </p>
    </div>
    <div class="contact-card">
      <h1 class="person-name">Marisol Vega, B.A.</h1>
      <p class="person-title">Board Certified Asst. Behavior Analyst<br>(BCABA)</p>
    </div>
    <div class="contact-lines">
      <p><span class="contact-label">Phone:</span> <span class="contact-value">786-555-0142</span></p>
      <p><span class="contact-label">E-mail:</span> <span class="contact-value">vega.m.aba@example.com</span></p>
    </div>
  </section>

</main>
</body>
</html>
```